Yacht, Boats, Watersports company needs a redesign of business card

Hello Designers!
We are a Boat dealership company that sells fun in the water, we sell boats, Yachts, Kayaks and also yacht WaterSport toys. We are looking to redesign our business cards in to something a little bit more sophisticated. in a way that we can make better use of our company colors. I'm attaching a zipped file containing the company 3 sets of company logo which one is an horizontal another one is a vertical and also a chromed 3d logo. Also is included two set of business cards that we use and also some designs that i think it's interesting. We use PMS 2026c Orange and PMS 7687C Blue. I would like to see at least two different options with the orange as accent and also using blue as an accent color. It's really important for the business cards to have a font option and size that is legible to most people. Our current website is wwww.corvellamarine.com. Please visit if you want to have a better feeling of the Boat dealership
You can send Single sided or double side options. We are now using single sided but we may be open for a double side option if we really like the design.
Target Market(s)
Marine, boat sales, yacht sales, water toys sales/
Contact Information for Business Card
Name: Dale Pritchett
Address: 718 West Halden Lane,
Dania Beach, FL 33019
Phone: 954-382-7146
Fax: 954:382-7139
Cell: 954-451-8320
Email: 212@corvellamarine.com
Website: corvellamarine.com
Requirements
Must have
- the current information of the business card provided.
logo
use the PMS Colors
Nice to have
- a touch of elegance and sophistication but simple
Should not have
- should not have any typography that is hard to read, the card should be simple but yet sophisticated.

```html
<!DOCTYPE html>
<html lang="en">
<head>
<meta charset="utf-8">
<title>Corvella Marine — Business Card</title>
<link rel="stylesheet" href="https://fonts.googleapis.com/css2?family=Oswald:wght@600&family=Roboto:wght@400;700&display=swap">
<style>
  :root {
    --navy: #0f4577;
    --orange: #e95d2c;
    --white: #ffffff;
    --paper: #f4f4f4;
    --backdrop: #e4e4e4;
  }
  * { margin: 0; padding: 0; box-sizing: border-box; }
  html, body { width: 1200px; height: 960px; overflow: hidden; }
  body {
    background: radial-gradient(ellipse at center, #efefef 0%, var(--backdrop) 70%, #dcdcdc 100%);
    font-family: "Roboto", Arial, sans-serif;
    position: relative;
  }
  .card {
    position: absolute;
    left: 307px;
    width: 590px;
    height: 335px;
    overflow: hidden;
    box-shadow: 3px 4px 6px rgba(0,0,0,0.35);
  }
  /* Front */
  .card-front { top: 118px; background: var(--navy); }
  .front-mark {
    position: absolute; left: 245px; top: 77px;
    width: 100px; height: 100px;
    border: 6px solid var(--orange); border-radius: 50%;
  }
  .front-name {
    position: absolute; left: 0; right: 0; top: 198px;
    text-align: center; color: var(--white);
    font-weight: 700; font-size: 27px; letter-spacing: 3px;
    text-transform: uppercase;
  }
  .front-web {
    position: absolute; left: 0; right: 0; top: 284px;
    text-align: center; font-size: 15px; letter-spacing: 2px;
    color: var(--white);
  }
  .front-web .domain { color: var(--orange); }
  .front-notch {
    position: absolute; left: 275px; bottom: 0;
    width: 0; height: 0;
    border-left: 20px solid transparent; border-right: 20px solid transparent;
    border-bottom: 28px solid var(--orange);
  }
  /* Back */
  .card-back { top: 505px; background: var(--paper); }
  .back-band {
    position: absolute; left: 0; top: 0; width: 100%; height: 123px;
    background: var(--navy); border-bottom: 2px solid var(--orange);
  }
  .back-name-mark {
    position: absolute; left: 0; right: 0; top: 22px;
    text-align: center; color: var(--white);
    font-weight: 700; font-size: 22px; letter-spacing: 3px;
    text-transform: uppercase;
  }
  .edge-tab { position: absolute; top: 102px; }
  .edge-tab.left { left: 0; }
  .edge-tab.right { right: 0; }
  .back-mark {
    position: absolute; left: 242px; top: 69px;
    width: 106px; height: 106px; border-radius: 50%;
    background: var(--white);
    display: flex; align-items: center; justify-content: center;
  }
  .back-mark span {
    width: 92px; height: 92px; border-radius: 50%;
    border: 6px solid var(--orange);
  }
  .person {
    position: absolute; left: 0; right: 0; top: 187px;
    text-align: center;
    font-family: "Oswald", "Arial Narrow", sans-serif;
    font-weight: 600; font-size: 27px; text-transform: uppercase;
    color: var(--navy);
  }
  .person .surname { color: var(--orange); }
  .contacts {
    position: absolute; left: 0; right: 0; top: 233px;
    text-align: center; color: var(--navy); font-size: 16px; line-height: 20px;
  }
  .contact-row { display: flex; justify-content: center; gap: 19px; }
  .contact-item { display: inline-flex; align-items: center; gap: 4px; }
  .contact-item svg { fill: var(--orange); }
  .rule {
    position: absolute; left: 85px; width: 420px; top: 280px;
    height: 2px; background: var(--orange);
  }
  .address {
    position: absolute; left: 0; right: 0; top: 289px;
    text-align: center; color: var(--navy); font-size: 16px;
  }
</style>
</head>
<body>

<section class="card card-front">
  <div class="front-mark"></div>
  <div class="front-name">Corvella Marine</div>
  <div class="front-web"><span class="domain">corvellamarine</span>.com</div>
  <div class="front-notch"></div>
</section>

<section class="card card-back">
  <div class="back-band"></div>
  <div class="back-name-mark">Corvella Marine</div>
  <svg class="edge-tab left" width="28" height="42" viewBox="0 0 28 42"><polygon points="0,0 28,21 0,42" fill="var(--orange)"/></svg>
  <svg class="edge-tab right" width="28" height="42" viewBox="0 0 28 42"><polygon points="28,0 0,21 28,42" fill="var(--orange)"/></svg>
  <div class="back-mark"><span></span></div>

  <div class="person">Dale <span class="surname">Pritchett</span></div>

  <div class="contacts">
    <div class="contact-row">
      <span class="contact-item">
        <svg width="14" height="14" viewBox="0 0 24 24"><path d="M6.6 10.8a15.1 15.1 0 0 0 6.6 6.6l2.2-2.2c.3-.3.7-.4 1-.2 1.1.4 2.3.6 3.6.6.6 0 1 .4 1 1V20c0 .6-.4 1-1 1A17 17 0 0 1 3 4c0-.6.4-1 1-1h3.5c.6 0 1 .4 1 1 0 1.3.2 2.5.6 3.6.1.3 0 .7-.2 1z"/></svg>
        954-382-7146
      </span>
      <span class="contact-item">
        <svg width="15" height="14" viewBox="0 0 24 22"><rect x="6" y="0" width="12" height="6"/><rect x="0" y="7" width="24" height="10" rx="2"/><rect x="6" y="14" width="12" height="8" fill="var(--paper)" stroke="var(--orange)" stroke-width="2"/></svg>
        954:382-7139
      </span>
      <span class="contact-item">
        <svg width="10" height="15" viewBox="0 0 14 22"><path d="M2 0h10a2 2 0 0 1 2 2v18a2 2 0 0 1-2 2H2a2 2 0 0 1-2-2V2a2 2 0 0 1 2-2zm0 3v14h10V3zm5 15.5a1.2 1.2 0 1 0 0 2.4 1.2 1.2 0 0 0 0-2.4z"/></svg>
        954-451-8320
      </span>
    </div>
    <div class="contact-row">
      <span class="contact-item">
        <svg width="14" height="11" viewBox="0 0 24 18"><path d="M0 0h24v18H0zm2 2v1l10 7 10-7V2zm0 3.4V16h20V5.4l-10 7z"/></svg>
        212@corvellamarine.com
      </span>
    </div>
  </div>

  <div class="rule"></div>
  <div class="address">718 West Halden Lane, Dania Beach, FL 33019</div>
</section>

</body>
</html>
```